Home Remodeling company needs a business card design

we need a business card design for home remodeling company in hamilton county, indiana USA. we offers a wide range of construction services including whole house renovations, Design and Build Basements and Kitchen and Bathroom Remodeling . we would like to see designs for both site of business card that use the same color of the company logo and also including all information below :
1- Tarek Salim CEO / General Contractor
2- all company contacts Telephone numbers ( 1-888-VOLMI-15 ) ( 317-555-0192) email address ( info@volmihome.example) website ( www.volmihome.example ) and social media logos (Facebook- twitter- google plus )
3- company logo
4- licensed . insured . bonded

```html
<!DOCTYPE html>
<html lang="en">
<head>
<meta charset="utf-8">
<title>Volmi Business Card</title>
<link rel="stylesheet" href="https://fonts.googleapis.com/css2?family=Montserrat:wght@800&family=Arimo:wght@400&family=Libre+Bodoni:wght@400&display=swap">
<style>
  :root {
    --bg: #d9d9d9;
    --card-white: #ffffff;
    --card-black: #000000;
    --brand-red: #c8323b;
    --brand-grey: #8f979a;
    --ink: #333333;
    --text: #111111;
  }
  * { margin: 0; padding: 0; box-sizing: border-box; }
  html, body { width: 1189px; height: 1200px; overflow: hidden; background: var(--bg); }
  .canvas { position: relative; width: 1189px; height: 1200px; }
  .card {
    position: absolute; left: 136px; width: 917px; height: 523px; overflow: hidden;
  }
  .card--front { top: 30px; background: var(--card-white); }
  .card--back { top: 640px; background: var(--card-black); }
  .card__swoosh { position: absolute; inset: 0; }

  .brand { position: absolute; display: flex; align-items: center; gap: 16px; }
  .brand__mark { width: 22px; height: 22px; background: var(--brand-red); }
  .brand__name {
    font-family: "Montserrat", sans-serif; font-weight: 800; letter-spacing: 6px; line-height: 1;
  }
  .card--front .brand { right: 92px; top: 52px; }
  .card--front .brand__name { font-size: 84px; color: var(--ink); }
  .card--back .brand { left: 50%; top: 50%; transform: translate(-50%, -50%); }
  .card--back .brand__name { font-size: 104px; color: #ffffff; }
  .card--back .brand__mark { width: 28px; height: 28px; }

  .credentials {
    position: absolute; right: 92px; top: 150px;
    font-family: "Arimo", sans-serif; font-size: 25px; color: var(--text);
  }
  .social { position: absolute; left: 629px; top: 214px; display: flex; gap: 16px; }
  .social__tile { width: 55px; height: 50px; border-radius: 5px; }
  .social__tile--dark { background: #23235a; }
  .social__tile--sky { background: #2aa3de; }
  .social__tile--red { background: var(--brand-red); }

  .person { position: absolute; left: 45px; top: 252px; }
  .person__name {
    font-family: "Libre Bodoni", serif; font-size: 46px; color: var(--brand-red); line-height: 1;
  }
  .person__title {
    margin-top: 8px; font-family: "Arimo", sans-serif; font-size: 25px; color: var(--text);
  }
  .contacts { position: absolute; left: 45px; top: 358px; list-style: none; }
  .contacts__item {
    display: flex; align-items: center; gap: 14px; height: 32px;
    font-family: "Arimo", sans-serif; font-size: 25px; color: var(--text);
  }
  .contacts__icon { width: 21px; height: 21px; flex: none; }
</style>
</head>
<body>
<main class="canvas">
  <section class="card card--front">
    <svg class="card__swoosh" width="917" height="523" viewBox="0 0 917 523" aria-hidden="true">
      <path d="M0 0 H330 Q95 70 0 260 Z" fill="var(--brand-grey)"/>
      <path d="M0 0 H272 Q60 80 0 218 Z" fill="var(--brand-red)"/>
      <path d="M917 40 Q835 420 528 523 H917 Z" fill="var(--brand-grey)"/>
      <path d="M917 80 Q858 440 565 523 H917 Z" fill="var(--brand-red)"/>
    </svg>

    <div class="brand">
      <span class="brand__mark"></span>
      <span class="brand__name">VOLMI</span>
    </div>
    <p class="credentials">licensed .insured . bonded</p>

    <div class="social" aria-label="Social media links">
      <span class="social__tile social__tile--dark"></span>
      <span class="social__tile social__tile--sky"></span>
      <span class="social__tile social__tile--red"></span>
    </div>

    <div class="person">
      <h1 class="person__name">Tarek Salim</h1>
      <p class="person__title">CEO / General Contractor</p>
    </div>

    <ul class="contacts">
      <li class="contacts__item">
        <svg class="contacts__icon" viewBox="0 0 20 20" aria-hidden="true"><rect width="20" height="20" fill="var(--brand-red)"/><path d="M6 4 L9 4 L9 7 L7.5 8 Q8.5 11.5 12 12.5 L13 11 L16 11 L16 14 Q10 16 6 10 Q4.5 7 6 4 Z" fill="#fff"/></svg>
        <span>317-555-0192</span>
      </li>
      <li class="contacts__item">
        <svg class="contacts__icon" viewBox="0 0 20 20" aria-hidden="true"><rect width="20" height="20" fill="var(--brand-red)"/><path d="M6 4 L9 4 L9 7 L7.5 8 Q8.5 11.5 12 12.5 L13 11 L16 11 L16 14 Q10 16 6 10 Q4.5 7 6 4 Z" fill="#fff"/></svg>
        <span>1-888-VOLMI-15</span>
      </li>
      <li class="contacts__item">
        <svg class="contacts__icon" viewBox="0 0 20 20" aria-hidden="true"><rect width="20" height="20" fill="var(--brand-red)"/><circle cx="10" cy="10" r="6" fill="none" stroke="#fff" stroke-width="1.6"/><path d="M4 10 H16 M10 4 Q6.5 10 10 16 M10 4 Q13.5 10 10 16" fill="none" stroke="#fff" stroke-width="1.2"/></svg>
        <span>www.volmihome.example</span>
      </li>
      <li class="contacts__item">
        <svg class="contacts__icon" viewBox="0 0 20 20" aria-hidden="true"><rect width="20" height="20" fill="var(--brand-red)"/><rect x="3.5" y="6" width="13" height="9" fill="none" stroke="#fff" stroke-width="1.4"/><path d="M3.5 6 L10 11 L16.5 6" fill="none" stroke="#fff" stroke-width="1.4"/></svg>
        <span>info@volmihome.example</span>
      </li>
    </ul>
  </section>

  <section class="card card--back">
    <div class="brand">
      <span class="brand__mark"></span>
      <span class="brand__name">VOLMI</span>
    </div>
  </section>
</main>
</body>
</html>
```